Letterhead creation for military law attorney

I need letterhead design for my business. We are now only doing military law and need to change address, logo and vision. I like the idea of using an eagle or a jolly roger flag

Target Market(s)

Military Law Clients

Colors
3176b5
85abd2

Requirements
Must have
• We are defending people against the government
Nice to have
• Jolly Roger Flag

```html
<!DOCTYPE html>
<html lang="en">
<head>
<meta charset="utf-8">
<title>Harlan Defense PLLC – Letterhead</title>
<link href="https://fonts.googleapis.com/css2?family=Open+Sans:wght@400;600;700&display=swap" rel="stylesheet">
<style>
  :root {
    --backdrop: #cbcbcb;
    --paper: #fafafa;
    --paper-edge: #6d6d6d;
    --ink-strong: #1a1a1a;
    --ink-body: #6a6a6a;
    --ink-footer: #2b2b2b;
    --band-dark: #0b0b0b;
    --band-grey: #404245;
    --band-text: #ffffff;
    --signature: #2e2a7a;
  }
  * { margin: 0; padding: 0; box-sizing: border-box; }
  html, body {
    width: 994px; height: 1200px; overflow: hidden;
    background: var(--backdrop);
    font-family: "Open Sans", sans-serif;
  }
  .letterhead {
    position: absolute; left: 196px; top: 175px;
    width: 600px; height: 849px;
    background: var(--paper);
    border: 1px solid var(--paper-edge);
  }
  .brand {
    position: absolute; top: 62px; left: 0; right: 0;
    text-align: center; color: var(--ink-strong);
  }
  .brand-name {
    display: inline-flex; align-items: center; gap: 8px;
    font-size: 19px; font-weight: 400; letter-spacing: 1.6px;
    line-height: 24px;
  }
  .brand-mark {
    width: 12px; height: 12px; border-radius: 50%;
    background: var(--ink-strong);
  }
  .brand-sub {
    margin-top: 0;
    display: flex; justify-content: center; align-items: center; gap: 6px;
    font-size: 11px; letter-spacing: 2.4px;
  }
  .brand-sub::before, .brand-sub::after {
    content: ""; width: 56px; height: 1px; background: var(--ink-strong);
  }
  .letter-body {
    position: absolute; left: 60px; top: 205px; width: 481px;
    font-size: 8.75px; line-height: 15.3px; color: var(--ink-body);
  }
  .salutation { margin-bottom: 29px; }
  .letter-body p.copy { text-align: justify; margin-bottom: 15.3px; }
  .sign-off {
    position: absolute; left: 60px; top: 574px;
    font-size: 8.6px; color: var(--ink-body);
  }
  .sign-name { font-weight: 700; color: #555; }
  .signature {
    display: block; margin: 12px 0 6px;
    width: 146px; height: 30px;
  }
  .contact {
    position: absolute; left: 0; right: 0; top: 752px;
    text-align: center; color: var(--ink-footer);
    font-size: 10.8px; line-height: 19px;
  }
  .contact-line { display: flex; justify-content: center; align-items: center; gap: 4px; }
  .contact-line svg { width: 11px; height: 11px; }
  .web-band {
    position: absolute; left: 0; right: 0; top: 800px; height: 26px;
    background: linear-gradient(to right, var(--band-dark) 50%, var(--band-grey) 50%);
    color: var(--band-text); font-size: 10.8px;
    display: flex; align-items: center; justify-content: center;
  }
</style>
</head>
<body>
  <main class="letterhead">
    <header class="brand">
      <div class="brand-name"><span class="brand-mark"></span>HARLAN DEFENSE</div>
      <div class="brand-sub">PLLC</div>
    </header>

    <section class="letter-body">
      <p class="salutation">Dear Sir,</p>
      <p class="copy">Lorem Ipsum is simply dummy text of the printing and typesetting industry. Lorem Ipsum has been the industry's standard dummy text ever since the 1500s, when an unknown printer took a galley of type and scrambled it to make a type specimen book. It has survived not only five centuries, but also the leap into electronic typesetting, remaining essentially unchanged. It was popularised in the 1960s with the release of Lettrafold sheets containing Lorem Ipsum passages, and more recently with desktop publishing software like Quillon PageBuilder including versions of Lorem Ipsum.</p>
      <p class="copy">Lorem Ipsum is simply dummy text of the printing and typesetting industry. Lorem Ipsum has been the industry's standard dummy text ever since the 1500s, when an unknown printer took a galley of type and scrambled it to make a type specimen book. It has survived not only five centuries, but also the leap into electronic typesetting, remaining essentially unchanged. It was popularised in the 1960s with the release of Lettrafold sheets containing Lorem Ipsum passages, and more recently with desktop publishing software like Quillon PageBuilder including versions of Lorem Ipsum.</p>
      <p class="copy">Lorem Ipsum is simply dummy text of the printing and typesetting industry. Lorem Ipsum has been the industry's standard dummy text ever since the 1500s, when an unknown printer took a galley of type and scrambled it to make a type specimen book.</p>
    </section>

    <section class="sign-off">
      <p class="sign-name">Your Name</p>
      <svg class="signature" role="img" aria-label="Handwritten signature of Marcus Ellery" viewBox="0 0 146 30">
        <rect x="0" y="6" width="146" height="18" rx="9" fill="var(--signature)" opacity="0.18"/>
      </svg>
      <p class="sign-title">CEO &nbsp;|&nbsp; Owner</p>
    </section>

    <footer class="contact">
      <p>PO Box 218 Riverton, TN 37000</p>
      <p class="contact-line">
        <svg viewBox="0 0 12 12"><circle cx="6" cy="6" r="5.4" fill="none" stroke="currentColor" stroke-width="0.9"/><path d="M3.6 4.4c0-.5.4-.9.9-.9h3c.5 0 .9.4.9.9v.5H7.2v-.6H4.8v.6H3.6z M4.2 5.4h3.6l.6 2.8H3.6z" fill="currentColor"/></svg>
        <span>(555) 014-2870</span>
        <svg viewBox="0 0 12 12"><circle cx="6" cy="6" r="5.4" fill="none" stroke="currentColor" stroke-width="0.9"/><rect x="3.2" y="4" width="5.6" height="4" fill="currentColor"/><path d="M3.2 4L6 6.2 8.8 4" fill="none" stroke="#fff" stroke-width="0.6"/></svg>
        <span>(555) 014-2871</span>
        <svg viewBox="0 0 12 12"><circle cx="6" cy="6" r="5.4" fill="none" stroke="currentColor" stroke-width="0.9"/><circle cx="6" cy="6" r="3" fill="none" stroke="currentColor" stroke-width="0.7"/><path d="M3 6h6M6 3v6" stroke="currentColor" stroke-width="0.6"/></svg>
        <span>info@harlandefensepllc.com</span>
      </p>
    </footer>

    <div class="web-band">www.HARLANDEFENSEPLLC.com</div>
  </main>
</body>
</html>
```